Business Card Design

Electrical Contracting buisness
need a buisness card relating to that buisness

Reason: Just need to discuss with partner

Industry/Entity Type

Business

Contact Information for Business Card

Colin Harbage Electrical
0417 562 983
colinharbage7@mailvessel.com
REC 48761

```html
<!DOCTYPE html>
<html lang="en">
<head>
<meta charset="utf-8">
<title>Colin Harbage Electrical — Business Card</title>
<link href="https://fonts.googleapis.com/css2?family=Exo+2:wght@400;500;600&display=swap" rel="stylesheet">
<style>
  :root {
    --page-bg: #e6e8ec;
    --card-white: #ffffff;
    --card-shade: #eceef0;
    --blue-light: #1aa3e8;
    --blue-mid: #1b7fd6;
    --blue-deep: #1f5fbf;
    --band-grey: #a9abae;
    --brand-blue: #1f6fd0;
    --text-on-blue: #ffffff;
  }
  * { margin: 0; padding: 0; box-sizing: border-box; }
  html, body {
    width: 1200px; height: 900px; overflow: hidden;
    background: var(--page-bg);
    font-family: "Exo 2", "Segoe UI", sans-serif;
  }
  .business-card {
    position: absolute; left: 150px; top: 193px;
    width: 900px; height: 514px;
    border-radius: 44px; overflow: hidden;
    background: var(--card-white);
    box-shadow: 0 18px 40px rgba(30, 40, 60, 0.18);
  }
  .card-shapes { position: absolute; inset: 0; }
  .brand-block {
    position: absolute; left: 40px; top: 190px; width: 330px;
    display: flex; flex-direction: column; align-items: center; gap: 18px;
  }
  .brand-dot {
    width: 64px; height: 64px; border-radius: 50%;
    background: var(--brand-blue);
  }
  .brand-name {
    color: var(--brand-blue); font-weight: 500;
    font-size: 30px; line-height: 1.15; letter-spacing: 1px;
    text-transform: uppercase; text-align: center;
  }
  .contact-block {
    position: absolute; right: 44px; top: 46px;
    color: var(--text-on-blue); text-align: right;
  }
  .person-name { font-size: 27px; font-weight: 500; letter-spacing: 1.5px; text-transform: uppercase; }
  .person-role { font-size: 17px; font-weight: 400; letter-spacing: 1.5px; text-transform: uppercase; margin-top: 4px; }
  .address { font-size: 20px; line-height: 1.3; margin-top: 44px; letter-spacing: 0.5px; }
  .contact-list { list-style: none; margin-top: 42px; }
  .contact-list li {
    display: flex; justify-content: flex-end; align-items: center; gap: 12px;
    font-size: 19px; letter-spacing: 0.8px; height: 38px;
  }
  .contact-list svg { width: 20px; height: 20px; flex: none; }
</style>
</head>
<body>
  <div class="business-card">
    <svg class="card-shapes" viewBox="0 0 900 514" aria-hidden="true">
      <defs>
        <radialGradient id="blue-panel" cx="0.45" cy="0.4" r="0.75">
          <stop offset="0" stop-color="var(--blue-light)"/>
          <stop offset="0.55" stop-color="var(--blue-mid)"/>
          <stop offset="1" stop-color="var(--blue-deep)"/>
        </radialGradient>
        <linearGradient id="white-panel" x1="0" y1="0" x2="1" y2="1">
          <stop offset="0" stop-color="var(--card-white)"/>
          <stop offset="1" stop-color="var(--card-shade)"/>
        </linearGradient>
      </defs>
      <rect width="900" height="514" fill="url(#white-panel)"/>
      <path class="grey-band" d="M300,0 C455,55 475,330 365,514 L900,514 L900,0 Z" fill="var(--band-grey)"/>
      <path class="blue-panel" d="M330,0 C482,60 500,330 392,514 L900,514 L900,0 Z" fill="url(#blue-panel)"/>
    </svg>

    <div class="brand-block">
      <span class="brand-dot"></span>
      <div class="brand-name">Colin Harbage<br>Electrical</div>
    </div>

    <div class="contact-block">
      <div class="person-name">Dana Rowell</div>
      <div class="person-role">President</div>
      <div class="address">14 Foundry Lane, Unit 3<br>Ringwood</div>
      <ul class="contact-list">
        <li>03 9870 4415
          <svg viewBox="0 0 20 20"><path d="M5 2 L8 6 L6.5 8 C7.5 10.5 9.5 12.5 12 13.5 L14 12 L18 15 L16 18 C9 18 2 11 2 4 Z" fill="#fff"/></svg>
        </li>
        <li>0417 562 983
          <svg viewBox="0 0 20 20"><rect x="5" y="1" width="10" height="18" rx="2" fill="none" stroke="#fff" stroke-width="1.8"/><circle cx="10" cy="15.5" r="1.2" fill="#fff"/></svg>
        </li>
        <li>03 9870 4416
          <svg viewBox="0 0 20 20"><rect x="3" y="8" width="14" height="9" rx="1.5" fill="#fff"/><rect x="6" y="2" width="8" height="7" fill="none" stroke="#fff" stroke-width="1.6"/></svg>
        </li>
        <li>colinharbage7@mailvessel.com
          <svg viewBox="0 0 20 20"><rect x="2" y="4" width="16" height="12" rx="1" fill="#fff"/><path d="M2.5 4.5 L10 11 L17.5 4.5" fill="none" stroke="#1f6fd0" stroke-width="1.5"/></svg>
        </li>
        <li>www.harbageelectric.com.au
          <svg viewBox="0 0 20 20"><circle cx="10" cy="10" r="8" fill="none" stroke="#fff" stroke-width="1.6"/><ellipse cx="10" cy="10" rx="3.5" ry="8" fill="none" stroke="#fff" stroke-width="1.3"/><path d="M2 10 H18 M3.5 6 H16.5 M3.5 14 H16.5" stroke="#fff" stroke-width="1.2"/></svg>
        </li>
      </ul>
    </div>
  </div>
</body>
</html>
```